Velorix Flyer

PROJECT: Digital Flyer for VeloRix

Format
1920 × 1080 px (landscape, optimized for presentations and email)
Deliverables
• PDF
• PNG

About VeloRix
VeloRix is a Dutch B2B software company providing a unified CRM and customer journey platform. We help businesses manage the entire customer lifecycle — from first contact to loyal customer — by centralizing all touchpoints in one system.
What sets us apart:
Extreme ease of use. The system is self-guiding, shows only what's relevant per employee, and requires virtually no training. All channels (email, phone, chat, in-store) come together in one place with automatic task distribution. Built-in AI functions as a smart digital colleague that continuously learns.
Target audience:
Directors and sales managers at B2B companies with multiple customer contact channels.

Goal:
We want to create a flyer that sets us apart from other CRM platform providers. Our aim is to achieve this through simplicity and a professional appearance. The design should reflect our core value: ease of use. The recipient should feel compelled to engage with us — not overwhelmed by information, but intrigued by clarity. Less is more.

Required Text Elements
Headline:
"CRM that adapts to how you work"
Subline:
"Discover how VeloRix simplifies your sales process"
Call-to-action:
"See it in action — book a call"
Contact details:
• hello@velorix.nl
• 023-5718469
• velorix.com

Required Visual Elements
• VeloRix logo (attached)

Design Style
• Modern / Minimalist
• Professional / Business
• Tech / Futuristic
• Clean with plenty of whitespace

Tone of voice:
Clear, positive and customer-focused. Practical and accessible business style aimed at communicating concrete value for users.

Design inspiration — please review these websites:
• orbantal.com
• ravelo.app
• quendo.com
• tirameld.com
• gonwisp.com
What We DON'T Want
• Bold / In-your-face
• Dense / Compact
• Trendy / Experimental
• Childlike / Cheerful
• Playful / Cartoonish
• Busy / Chaotic
Colors
Use the color palette from velorix.com (blues, whites, clean professional tones).
[Exact hex codes used for element on the website:
#344054;
#1a1b1f;
#0254ac
#002249;
#e5edf7;
background-color: #fff; ]
Competitors (for context only — do NOT copy)
• brinvolt.nl
• kelmarin.com
• dortavecrm.com
• wexalunda.com
Budget
$150
Deadline
January 26, 2026

```html
<!DOCTYPE html>
<html lang="en">
<head>
<meta charset="UTF-8">
<title>Velorix Flyer</title>
<link href="https://fonts.googleapis.com/css2?family=Outfit:wght@500;600;700&display=swap" rel="stylesheet">
<style>
  :root {
    --navy: #12235a;
    --sky: #1aa3de;
    --white: #ffffff;
  }
  * { margin: 0; padding: 0; box-sizing: border-box; }
  html, body { width: 1200px; height: 675px; overflow: hidden; background: var(--white); }
  .flyer {
    position: relative;
    width: 1200px;
    height: 675px;
    background: var(--white);
    font-family: "Outfit", sans-serif;
    color: var(--navy);
    overflow: hidden;
  }
  .brand {
    position: absolute;
    left: 64px;
    top: 96px;
    display: flex;
    align-items: center;
    gap: 12px;
  }
  .brand-dot {
    width: 30px; height: 30px;
    border-radius: 50%;
    background: var(--navy);
  }
  .brand-name {
    font-weight: 700;
    font-size: 38px;
    color: var(--navy);
    letter-spacing: -0.5px;
  }
  .headline {
    position: absolute;
    left: 62px;
    top: 222px;
    font-weight: 600;
    font-size: 70px;
    line-height: 73px;
    letter-spacing: -0.5px;
    color: var(--navy);
  }
  .subline {
    position: absolute;
    left: 65px;
    top: 386px;
    font-weight: 600;
    font-size: 22.5px;
    color: var(--navy);
  }
  .cta {
    position: absolute;
    left: 64px;
    top: 472px;
    font-weight: 500;
    font-size: 21px;
    color: var(--sky);
  }
  .contact-label {
    position: absolute;
    left: 67px;
    top: 518px;
    width: 124px;
    height: 23px;
    border-radius: 6px;
    background: var(--sky);
    color: var(--white);
    font-weight: 500;
    font-size: 15px;
    line-height: 23px;
    text-align: center;
  }
  .contact-list {
    position: absolute;
    left: 64px;
    top: 559px;
    list-style: none;
  }
  .contact-item {
    position: absolute;
    display: flex;
    align-items: center;
    gap: 14px;
    white-space: nowrap;
    font-weight: 600;
    font-size: 13.5px;
    color: var(--sky);
  }
  .contact-item.phone { left: 0; }
  .contact-item.email { left: 153px; }
  .contact-item.web { left: 352px; top: -2px; }
  .contact-icon { width: 33px; height: 33px; flex: none; }
</style>
</head>
<body>
  <main class="flyer">
    <div class="brand">
      <span class="brand-dot"></span>
      <span class="brand-name">Velorix</span>
    </div>

    <h1 class="headline">CRM that adapts to<br>how you work</h1>
    <p class="subline">Discover how Velorix simplifies your sales process</p>

    <p class="cta">See it in action, book a call</p>
    <div class="contact-label">Contact detail</div>

    <ul class="contact-list">
      <li class="contact-item phone">
        <svg class="contact-icon" viewBox="0 0 33 33" aria-hidden="true">
          <circle cx="16.5" cy="16.5" r="16.5" fill="#1aa3de"/>
          <path d="M11 9.5c1-.8 2-.6 2.6.4l1.3 2.3c.5.9.2 1.7-.6 2.3l-.8.6c.7 1.9 2.1 3.4 3.9 4.3l.7-.8c.6-.8 1.5-1 2.3-.5l2.2 1.4c.9.6 1 1.7.3 2.6l-.9 1c-1 1-2.6 1.2-4 .5-3.8-1.9-6.5-5-7.8-9-.4-1.4-.1-2.9.8-3.6z" fill="none" stroke="#fff" stroke-width="1.6" stroke-linejoin="round"/>
          <path d="M18 9.5a6 6 0 0 1 5.5 5.5M18 12.3a3.2 3.2 0 0 1 2.7 2.7" fill="none" stroke="#fff" stroke-width="1.5" stroke-linecap="round"/>
        </svg>
        <span>023-5718469</span>
      </li>
      <li class="contact-item email">
        <svg class="contact-icon" viewBox="0 0 33 33" aria-hidden="true">
          <circle cx="16.5" cy="16.5" r="16.5" fill="#1aa3de"/>
          <rect x="8" y="11" width="17" height="12" rx="1" fill="none" stroke="#fff" stroke-width="1.4"/>
          <path d="M8.5 11.5l8 6.5 8-6.5M8.5 22.5l6-5.5M24.5 22.5l-6-5.5" fill="none" stroke="#fff" stroke-width="1.3"/>
        </svg>
        <span>hello@velorix.nl</span>
      </li>
      <li class="contact-item web">
        <svg class="contact-icon" viewBox="0 0 33 33" aria-hidden="true">
          <circle cx="16.5" cy="16.5" r="16.5" fill="#1aa3de"/>
          <g fill="none" stroke="#fff" stroke-width="1.3">
            <circle cx="16.5" cy="16.5" r="8"/>
            <ellipse cx="16.5" cy="16.5" rx="3.6" ry="8"/>
            <path d="M8.5 16.5h16M9.6 12.5h13.8M9.6 20.5h13.8M16.5 8.5v16"/>
          </g>
        </svg>
        <span>velorix.com</span>
      </li>
    </ul>
  </main>
</body>
</html>
```